Corvane Electrical Solutions

On one side. LOGO (underneath:) Commercial Industrial Residential

- NAME & CONTACT DETAILS

Marcus T. Hollings
Project Manager

(Cell icon) (441) 582-6197
(Email icon) cvnelectricalsoultions@mailventra.com
(Facebook & Instagram icons )@cvnelectricalsolutions

Other side: LOGO - underneath ELECTRICAL CONSTRUCTION & MAINTENANCE . LED LIGHTING & AUTOMATION . LIFE SAFETY SYSTEMS (FIRE ALARM / SECURITY) . DATA & COMMUNICATION

```html
<!DOCTYPE html>
<html lang="en">
<head>
<meta charset="utf-8">
<title>Corvane Electrical Solutions – Business Card</title>
<link rel="stylesheet" href="https://fonts.googleapis.com/css2?family=Poppins:ital,wght@0,400;0,500;0,600;0,700;1,400;1,600&display=swap">
<style>
  :root {
    --teal: #1b5a70;
    --teal-deep: #154b5e;
    --teal-light: #236a80;
    --white: #ffffff;
    --ink: #4a4a4a;
    --backdrop: #2a2a2a;
  }
  * { box-sizing: border-box; margin: 0; padding: 0; }
  html, body {
    width: 1200px; height: 900px; overflow: hidden;
    background: var(--backdrop);
    font-family: "Poppins", sans-serif;
  }
  .stage {
    width: 1200px; height: 900px;
    display: flex; flex-direction: column; align-items: center; justify-content: center;
    gap: 46px;
  }
  .card {
    width: 660px; height: 377px; position: relative; overflow: hidden;
    box-shadow: 0 10px 28px rgba(0,0,0,.45);
  }

  /* Front */
  .card--front {
    background: linear-gradient(135deg, var(--teal-light), var(--teal) 55%, var(--teal-deep));
    color: var(--white);
  }
  .brand { display: flex; align-items: center; gap: 14px; position: absolute; }
  .brand__mark { width: 18px; height: 18px; background: currentColor; flex: none; }
  .brand__name {
    font-weight: 600; font-size: 27px; letter-spacing: 3px; text-transform: uppercase;
    line-height: 1.05;
  }
  .card--front .brand { left: 150px; top: 58px; }
  .front__rule {
    position: absolute; left: 44px; right: 44px; top: 178px;
    height: 1px; background: var(--white); opacity: .9;
  }
  .contacts {
    position: absolute; left: 44px; top: 196px;
    list-style: none; font-size: 14.5px; line-height: 1.75;
  }
  .contacts li { display: flex; align-items: center; gap: 10px; }
  .contacts svg { width: 15px; height: 15px; flex: none; }
  .social-dot { width: 11px; height: 11px; border: 1.6px solid var(--white); border-radius: 50%; flex: none; margin: 0 2px; }
  .person { position: absolute; right: 44px; top: 196px; text-align: right; }
  .person__name { font-weight: 600; font-size: 23px; }
  .person__role { font-weight: 400; font-size: 16px; letter-spacing: .5px; }
  .sectors {
    position: absolute; left: 0; right: 0; bottom: 34px; text-align: center;
    font-weight: 600; font-size: 14px; letter-spacing: 1.5px; text-transform: uppercase;
  }

  /* Back */
  .card--back { background: var(--white); }
  .card--back .brand { left: 110px; top: 72px; color: var(--teal); }
  .card--back .brand__name { font-size: 32px; }
  .services {
    position: absolute; left: 0; right: 0; bottom: 0; height: 128px;
    background: var(--teal); color: var(--white);
    display: flex; flex-direction: column; justify-content: center; align-items: center;
    font-weight: 500; font-size: 13px; letter-spacing: .8px; text-transform: uppercase;
    line-height: 1.8; text-align: center;
  }
</style>
</head>
<body>
<main class="stage">
  <section class="card card--front" aria-label="Business card front">
    <div class="brand">
      <span class="brand__mark"></span>
      <span class="brand__name">Corvane<br>Electrical<br>Solutions</span>
    </div>
    <div class="front__rule"></div>
    <ul class="contacts">
      <li>
        <svg viewBox="0 0 16 16" fill="none" stroke="currentColor" stroke-width="1.4"><rect x="4" y="1" width="8" height="14" rx="1.5"/><line x1="7" y1="12.5" x2="9" y2="12.5"/></svg>
        (441) 582-6197
      </li>
      <li>
        <svg viewBox="0 0 16 16" fill="currentColor"><path d="M1 3h14v10H1z"/><path d="M1 3l7 6 7-6" fill="none" stroke="var(--teal)" stroke-width="1.2"/></svg>
        cvnelectricalsoultions@mailventra.com
      </li>
      <li>
        <span class="social-dot"></span>
        @cvnelectricalsolutions
      </li>
    </ul>
    <div class="person">
      <p class="person__name">Marcus T. Hollings</p>
      <p class="person__role">Project Manager</p>
    </div>
    <p class="sectors">Commercial &bull; Industrial &bull; Residential</p>
  </section>

  <section class="card card--back" aria-label="Business card back">
    <div class="brand">
      <span class="brand__mark"></span>
      <span class="brand__name">Corvane<br>Electrical<br>Solutions</span>
    </div>
    <div class="services">
      <p>Electrical Construction &amp; Maintenance &bull; LED Lighting &amp; Automation</p>
      <p>Life Safety Systems (Fire Alarm / Security) &bull; Data &amp; Communication</p>
    </div>
  </section>
</main>
</body>
</html>
```